Quarrow financial services, is a financial company that provides consultancy, brokerage services, and funding.

we will be providing the clients with insights, knowledge and data with regards to the financial markets.

with the brokerage services we will try to find the suitable counterparts that provide them with the best investments that suits their needs and expected return.

Target Market(s)

financial institutions, Corporates, high-net worth individuals

Industry/Entity Type

Financial Service

Contact Information for Business Card

Font styles to use
Other font styles liked:
• applemyungjo

Colors
00a990
848484

Requirements
Must have
• the logo at the back
Nice to have
• Finesse
Should not have
• boldness

```html
<!DOCTYPE html>
<html lang="en">
<head>
<meta charset="utf-8">
<title>Quarrow Financial Services – Business Card</title>
<link href="https://fonts.googleapis.com/css2?family=Cinzel:wght@400&family=Source+Sans+3:wght@400&display=swap" rel="stylesheet">
<style>
  :root {
    --backdrop: #2e2e2e;
    --card-dark: #4d4d4d;
    --card-light: #ffffff;
    --ink-dark: #4a4a4a;
    --ink-light: #ffffff;
    --ink-muted: #a8a8a8;
    --accent-green: #7d9a4a;
    --mark-tint: #d3dec6;
    --divider-grey: #d4d4d4;
  }
  * { margin: 0; padding: 0; box-sizing: border-box; }
  html, body {
    width: 1200px; height: 900px; overflow: hidden;
    background: var(--backdrop);
  }
  .card {
    position: absolute; top: 301px;
    width: 514px; height: 296px;
  }
  .card--back { left: 72px; background: var(--card-dark); }
  .card--front { left: 615px; background: var(--card-light); }

  .brand {
    position: absolute; left: 18px; width: 230px; top: 70px;
    display: flex; flex-direction: column; align-items: center;
    font-family: "Cinzel", serif; font-weight: 400;
  }
  .brand__square { width: 52px; height: 52px; background: var(--mark-tint); margin-bottom: 46px; }
  .brand__name { font-size: 31px; letter-spacing: 1px; line-height: 1; }
  .brand__sub { font-size: 10.5px; letter-spacing: 1.8px; margin-top: 7px; }
  .card--back .brand { color: var(--ink-light); }
  .card--front .brand { color: var(--ink-dark); }

  .divider {
    position: absolute; left: 256px; top: 66px;
    width: 2px; height: 166px;
  }
  .card--back .divider { background: var(--accent-green); }
  .card--front .divider { background: var(--divider-grey); width: 1px; }

  .contact {
    position: absolute; left: 288px; top: 72px;
    color: var(--ink-dark);
    font-family: "Source Sans 3", sans-serif;
  }
  .contact__name {
    font-family: "Cinzel", serif; font-weight: 400; font-size: 16px; letter-spacing: 0.5px; line-height: 1.1;
  }
  .contact__role {
    font-family: "Cinzel", serif; font-size: 8.5px; letter-spacing: 1px; margin-top: 2px;
  }
  .contact__lines { margin-top: 26px; font-size: 11.5px; line-height: 14px; list-style: none; }
  .contact__label { color: var(--ink-muted); display: inline-block; width: 14px; }
  .contact__address { margin-top: 12px; font-size: 11.5px; line-height: 14.5px; font-style: normal; }
</style>
</head>
<body>
  <section class="card card--back" aria-label="Card back">
    <div class="brand">
      <span class="brand__square"></span>
      <span class="brand__name">QUARROW</span>
      <span class="brand__sub">FINANCIAL SERVICES</span>
    </div>
    <span class="divider"></span>
  </section>

  <section class="card card--front" aria-label="Card front">
    <div class="brand">
      <span class="brand__square"></span>
      <span class="brand__name">QUARROW</span>
      <span class="brand__sub">FINANCIAL SERVICES</span>
    </div>
    <span class="divider"></span>
    <div class="contact">
      <h1 class="contact__name">Daniel Harcourt</h1>
      <p class="contact__role">MANAGING DIRECTOR</p>
      <ul class="contact__lines">
        <li><span class="contact__label">p</span>212 490 37 18</li>
        <li><span class="contact__label">m</span>917 306 52 44</li>
        <li><span class="contact__label">e</span>d.harcourt@quarrowfinancial.com</li>
      </ul>
      <address class="contact__address">
        48 Linden Avenue<br>
        Brookfield, New York 10522<br>
        www.quarrowfinancial.com
      </address>
    </div>
  </section>
</body>
</html>
```